Tarnel-Holdings. Limestone; improving the world

New Limestone company and need logo design.
Limestone offsets carbon mitigation industries restore and replenish soil fertilities in the Prairies, the breadbasket of the world. At the same time, Limestone is proving a critical emergent component of carbon capture sequestration technology will therefore play a critical role in the development of the western Canadian energy industries
Our limestone resources are situated in the foothills of the Canadian Rockies well-positioned above the sprawling fields of the vast peace district.
Target Market(s)
Agriculture and oli sites
Logo Text
Tarnel Holdings
Number of Pages Required
3 page

```html
<!DOCTYPE html>
<html lang="en">
<head>
<meta charset="utf-8">
<title>Tarnel Holdings</title>
<link href="https://fonts.googleapis.com/css2?family=Poppins:wght@300;400;500;600;700&display=swap" rel="stylesheet">
<style>
:root{
  --green:#0b8a12;
  --blue:#0a19e6;
  --navy:#152244;
  --text:#4a4a4a;
  --grey-bg:#ececee;
  --teal:#3dbdc6;
  --violet:#5b69c6;
  --white:#ffffff;
}
*{margin:0;padding:0;box-sizing:border-box}
html,body{width:1200px;height:2795px;overflow:hidden;background:var(--white);font-family:'Poppins',sans-serif;color:var(--text)}
.page{position:relative;width:1200px;height:2795px}
.abs{position:absolute}

/* header */
.brand{left:142px;top:18px;font-weight:600;color:var(--green);line-height:1}
.brand .l1{font-size:50px;letter-spacing:1px;display:block}
.brand .l2{font-size:24px;display:block;margin-top:4px;letter-spacing:.5px}
.top-link{left:852px;top:30px;font-size:15px;color:#222}
.login{left:961px;top:29px;width:94px;height:22px;background:var(--blue);color:#fff;font-size:12px;text-align:center;line-height:22px}
.nav{right:144px;top:68px;display:flex;gap:22px;font-size:14px;color:#222;letter-spacing:.2px}

/* hero */
.hero{left:144px;top:111px;width:912px;height:477px;background:linear-gradient(135deg,#3fc1c7 0%,#4aa7c8 45%,#6f7dcf 100%)}
.hero-title{left:144px;top:282px;width:912px;text-align:center;color:#fff;font-weight:700;font-size:49px;line-height:49px;text-shadow:0 2px 6px rgba(0,0,0,.35)}
.btn-solid{left:445px;top:410px;width:150px;height:45px;background:var(--blue);color:#fff;font-weight:600;font-size:15px;text-align:center;line-height:45px}
.btn-ghost{left:605px;top:410px;width:149px;height:45px;border:2px solid #fff;color:#fff;font-weight:600;font-size:15px;text-align:center;line-height:41px}
.dots{display:flex;flex-direction:column;gap:8px}
.dots span{width:13px;height:13px;border-radius:50%;border:1.5px solid #fff}
.dots span.on{background:#fff}

/* welcome */
.frame{left:152px;top:665px;width:452px;height:382px;border:2px solid #6fbf6a;border-radius:14px}
.welcome-img{left:143px;top:673px;width:455px;height:382px;border-radius:14px;background:linear-gradient(180deg,#8ea6b8 0%,#d9a46c 35%,#8b6f55 60%,#a8583e 100%)}
.play{left:370px;top:848px;width:40px;height:28px;background:#e21d1d;border-radius:7px}
.welcome-kicker{left:646px;top:680px;font-size:33px;color:#333;font-weight:400}
.welcome-title{left:646px;top:724px;font-size:41px;font-weight:400;color:var(--green)}
.welcome-title .first{color:var(--blue)}
.welcome-copy{left:646px;top:792px;width:410px;font-size:14.5px;line-height:22.5px;font-weight:300;color:#444}
.btn-outline{left:646px;top:1003px;width:141px;height:41px;border:2px solid var(--blue);color:var(--blue);font-size:15px;text-align:center;line-height:37px}

/* news */
.section-title{width:1200px;left:0;text-align:center;font-weight:500;color:var(--navy);font-size:39px}
.card{top:1237px;width:285px;height:407px;background:#fff;box-shadow:0 2px 6px rgba(0,0,0,.12)}
.card .pic{height:192px}
.card .date{position:absolute;left:21px;top:133px;width:52px;height:40px;border-radius:6px;color:#fff;font-size:12.5px;font-weight:600;text-align:center;line-height:14px;padding-top:6px}
.card h3{position:absolute;left:15px;top:215px;width:260px;font-size:18px;font-weight:400;color:#222;line-height:22px}
.card p{position:absolute;left:15px;top:268px;width:262px;font-size:15px;font-weight:300;color:#444;line-height:22px}
.card .more{position:absolute;left:21px;top:351px;width:94px;height:22px;color:#fff;font-size:11px;text-align:center;line-height:22px}
.bg-blue{background:var(--blue)}
.bg-lblue{background:#3b4bf0}
.bg-green{background:var(--green)}

/* testimonials */
.testi{left:144px;top:1736px;width:912px;height:387px;background:linear-gradient(135deg,#3fc1c7 0%,#4fa9c9 50%,#6a75cc 100%)}
.testi-title{left:144px;top:1800px;width:912px;text-align:center;color:#fff;font-size:41px;font-weight:500}
.testi-copy{left:320px;top:1900px;width:600px;text-align:center;color:#fff;font-size:15px;line-height:27px;font-weight:300}
.testi-name{left:144px;top:2026px;width:912px;text-align:center;color:#fff;font-size:18px;font-weight:500}
.quote{color:rgba(255,255,255,.55);font-size:80px;font-family:Georgia,serif;line-height:1}

/* footer */
.footer{left:0;top:2205px;width:1200px;height:442px;background:var(--grey-bg)}
.foot-brand{left:142px;top:2262px;color:var(--green);font-weight:600;line-height:1}
.foot-brand .l1{font-size:72px;display:block;letter-spacing:1px}
.foot-brand .l2{font-size:36px;display:block;margin-top:4px}
.foot-copy{left:144px;top:2384px;width:320px;font-size:13.5px;line-height:22px;color:#444;font-weight:300}
.social{width:32px;height:32px;border-radius:50%;border:1.5px solid #555}
.foot-head{top:2276px;font-size:24px;color:#222;font-weight:400}
.field{left:525px;width:272px;background:#fff;border:1px solid #d6d6d6;font-size:13px;color:#777;padding:10px 14px}
.submit{left:525px;top:2552px;width:115px;height:36px;background:var(--blue);color:#fff;font-weight:600;font-size:14px;text-align:center;line-height:36px}
.contact-line{left:887px;font-size:14px;color:#222;line-height:21px}
.bottom{left:0;top:2647px;width:1200px;height:148px;background:linear-gradient(90deg,#178fd0 0%,#3a63c5 55%,#4a3fb9 100%)}
.bottom-links{left:0;top:2692px;width:1200px;text-align:center;color:#fff;font-size:16px;font-weight:500}
.bottom-copy{left:0;top:2731px;width:1200px;text-align:center;color:#fff;font-size:16px;font-weight:500}
</style>
</head>
<body>
<div class="page">

  <header>
    <div class="abs brand"><span class="l1">TARNEL</span><span class="l2">HOLDINGS</span></div>
    <div class="abs top-link">Contact Us</div>
    <div class="abs login">LOGO IN</div>
    <nav class="abs nav"><span>PRODUCTS</span><span>MARKETS</span><span>LOCATIONS</span><span>SUSTAINABILITY</span><span>ABOUT US</span><span>CAREERS</span></nav>
  </header>

  <section>
    <div class="abs hero" role="img" aria-label="Cargo ship in a harbour seen from above, tinted teal to violet"></div>
    <h1 class="abs hero-title">LOREM IPSUM IS SIMPLY<br>DUMMY TEXT</h1>
    <div class="abs btn-solid">LEARN MORE</div>
    <div class="abs btn-ghost">INVEST NOW</div>
    <div class="abs dots" style="left:1014px;top:313px"><span class="on"></span><span></span><span></span><span></span></div>
  </section>

  <section>
    <div class="abs frame"></div>
    <div class="abs welcome-img" role="img" aria-label="Container port with stacked shipping containers and cranes at sunset"></div>
    <div class="abs play"><svg width="40" height="28"><polygon points="17,9 17,19 25,14" fill="#fff"/></svg></div>
    <div class="abs welcome-kicker">Welcome to</div>
    <h2 class="abs welcome-title"><span class="first">Tarnel</span> Holdings</h2>
    <p class="abs welcome-copy">Sed ut perspiciatis unde omnis iste natus error sit voluptatem accusantium doloremque laudantium, totam rem aperiam, eaque ipsa quae ab illo inventore veritatis et quasi architecto beatae vitae dicta sunt explicabo. Nemo enim ipsam voluptatem quia voluptas sit aspernatur aut odit aut fugit, sed quia consequuntur magni dolores eos qui ratione voluptatem sequi nesciunt. Neque porro quisquam est</p>
    <div class="abs btn-outline">READ MORE</div>
  </section>

  <section>
    <h2 class="abs section-title" style="top:1160px">Latest News</h2>
    <svg class="abs" style="left:84px;top:1420px" width="26" height="48"><polyline points="24,2 2,24 24,46" fill="none" stroke="#555" stroke-width="2"/></svg>
    <svg class="abs" style="left:1092px;top:1420px" width="26" height="48"><polyline points="2,2 24,24 2,46" fill="none" stroke="#555" stroke-width="2"/></svg>

    <article class="abs card" style="left:144px">
      <div class="pic" role="img" aria-label="Green stock ticker display on a black screen" style="background:linear-gradient(135deg,#0e1a10,#1f3b1c 60%,#0a120a)"></div>
      <div class="date bg-blue">APR<br>05, 21</div>
      <h3>Nemo enim ipsam voluptate quia voluptas sit</h3>
      <p>Sed ut perspiciatis unde omnis iste natus sit voluptatem accusantium doloremque laudantium</p>
      <div class="more bg-lblue">READ MORE</div>
    </article>
    <article class="abs card" style="left:458px">
      <div class="pic" role="img" aria-label="Metal barrels, gold bars and silver ingots on a financial chart" style="background:linear-gradient(135deg,#4a4540,#9a9590 50%,#c9b27a)"></div>
      <div class="date bg-green">APR<br>05, 21</div>
      <h3>Nemo enim ipsam voluptate quia voluptas sit</h3>
      <p>Sed ut perspiciatis unde omnis iste natus sit voluptatem accusantium doloremque laudantium</p>
      <div class="more bg-green">READ MORE</div>
    </article>
    <article class="abs card" style="left:771px">
      <div class="pic" role="img" aria-label="Grain silos with an orange truck under a blue sky" style="background:linear-gradient(180deg,#6c9bd8 0%,#a9b8c6 55%,#c8843c 85%,#9a8a78)"></div>
      <div class="date bg-blue">APR<br>05, 21</div>
      <h3>Nemo enim ipsam voluptate quia voluptas sit</h3>
      <p>Sed ut perspiciatis unde omnis iste natus sit voluptatem accusantium doloremque laudantium</p>
      <div class="more bg-lblue">READ MORE</div>
    </article>
  </section>

  <section>
    <div class="abs testi" role="img" aria-label="Oil barrels and pipes, tinted teal to violet"></div>
    <h2 class="abs testi-title">Client Testimonials</h2>
    <div class="abs quote" style="left:282px;top:1896px">&ldquo;</div>
    <p class="abs testi-copy">Sed ut perspiciatis unde omnis iste natus error sit voluptatem accusantium doloremque laudantium, totam rem aperiam, eaque ipsa quae ab illo inventore veritatis et quasi architecto beatae vitae dicta sunt explicabo. Nemo enim ipsam voluptatem quia voluptas sit</p>
    <div class="abs testi-name">Marcel Dunford - Alberta</div>
    <div class="abs quote" style="left:778px;top:2010px">&rdquo;</div>
    <div class="abs dots" style="left:1017px;top:1893px"><span class="on"></span><span></span><span></span><span></span></div>
  </section>

  <footer>
    <div class="abs footer"></div>
    <div class="abs foot-brand"><span class="l1">TARNEL</span><span class="l2">HOLDINGS</span></div>
    <p class="abs foot-copy">Lorem ipsum dolor sit amet, consectetur aiscing elit, sed do eiusmod tempor incididunt ut labore et dolore magna aliqua. Ut enim ad minim niam, quis nostrud exercitation ullamco laboris nisi ut aliquip ex ea commodo consequat. Duis aute irure dolor in reprehenderit in voluptate</p>
    <div class="abs social" style="left:146px;top:2542px"></div>
    <div class="abs social" style="left:190px;top:2542px"></div>
    <div class="abs social" style="left:234px;top:2542px"></div>

    <h3 class="abs foot-head" style="left:525px">GET IN TOUCH</h3>
    <div class="abs field" style="top:2335px;height:39px">First Name</div>
    <div class="abs field" style="top:2384px;height:39px">Last Name</div>
    <div class="abs field" style="top:2432px;height:39px">Email</div>
    <div class="abs field" style="top:2480px;height:55px">Comments</div>
    <div class="abs submit">SUBMIT</div>

    <h3 class="abs foot-head" style="left:852px">CONTACT US</h3>
    <svg class="abs" style="left:856px;top:2336px" width="16" height="22"><path d="M8 1a7 7 0 0 0-7 7c0 5 7 13 7 13s7-8 7-13a7 7 0 0 0-7-7z" fill="#1d2a4a"/><circle cx="8" cy="8" r="2.6" fill="#ececee"/></svg>
    <div class="abs contact-line" style="top:2335px;font-size:13.5px">Tarnel Holdings<br>218 Ridgeline Road, Calgary<br>Alberta, T2P 1K4.</div>
    <svg class="abs" style="left:855px;top:2409px" width="18" height="18"><path d="M4 1l3 0 2 4-2 2c1 2 3 4 5 5l2-2 4 2v3c0 1-1 2-2 2C8 17 1 10 1 3c0-1 1-2 3-2z" fill="#1d2a4a"/></svg>
    <div class="abs contact-line" style="top:2406px;font-size:15px">Phone:<br>403-555-0187</div>
    <svg class="abs" style="left:855px;top:2470px" width="18" height="14"><rect x="0" y="0" width="18" height="14" rx="1" fill="#1d2a4a"/><polyline points="1,1 9,8 17,1" fill="none" stroke="#ececee" stroke-width="1.5"/></svg>
    <div class="abs contact-line" style="top:2465px;font-size:15px">Email:<br>hello@tarnelholdings.example</div>

    <div class="abs bottom"></div>
    <div class="abs bottom-links">Home &nbsp;|&nbsp; About Us &nbsp;|&nbsp; Investments &nbsp;|&nbsp; Our Services &nbsp;|&nbsp; Contact</div>
    <div class="abs bottom-copy">Tarnel Holdings © 2021 All Rights Reserved | Privacy Policy | Terms and Conditions</div>
  </footer>

</div>
</body>
</html>
```